Bramwick Client Journey To Success

I need a one-page document that graphically shows the client's journey working with Bramwick from initial assessment to completed project. I want the journey to start at the "basecamp logo" and reach 4 summits (little mountain logos...) .

I'd like the imagery to convey the client starting at basecamp, and moving to each summit. Each summit, should list the subtext under each, as listed on the pdf doc i provided.

The description for the basecamp and 4 summits is attached.

I need the brochure to look like the other brochure that you did for me (attached) .

Target Market(s)

Restaurant Owners

Industry/Entity Type

Construction Management

Font styles to use
Sans Serif

Colors
EB3D1F
EC4F4E
F09395
F8D3D4
FCEDEE

Requirements
Must have
• My logo. Title: Client Journey To Success. Subtitle: The 4 Summits

```html
<!DOCTYPE html>
<html lang="en">
<head>
<meta charset="utf-8">
<title>Bramwick Development – Client Journey: 4 Summits</title>
<link rel="stylesheet" href="https://fonts.googleapis.com/css2?family=Montserrat:wght@500;600;700;800;900&display=swap">
<style>
  :root {
    --stage: #2d2d2f;
    --paper: #ffffff;
    --red-bright: #ea3430;
    --red-deep: #b71f2a;
    --red-label: #c4222c;
    --ink: #2b2b2b;
    --rule: #8a8a8a;
  }
  html, body {
    margin: 0;
    width: 1200px;
    height: 1200px;
    overflow: hidden;
    background: var(--stage);
  }
  .flyer {
    position: absolute;
    left: 196px;
    top: 30px;
    width: 807px;
    height: 1140px;
    display: block;
    box-shadow: 0 10px 30px rgba(0,0,0,.45);
  }
  .title-small { font-family: 'Montserrat', sans-serif; font-weight: 600; fill: #fff; }
  .title-large { font-family: 'Montserrat', sans-serif; font-weight: 900; fill: #fff; }
  .brand-name { font-family: 'Montserrat', sans-serif; font-weight: 800; fill: var(--ink); }
  .stage-name { font-family: 'Montserrat', sans-serif; font-weight: 800; fill: #fff; text-anchor: middle; }
  .stage-num { font-family: 'Montserrat', sans-serif; font-weight: 900; fill: #fff; text-anchor: middle; }
  .step { font-family: 'Montserrat', sans-serif; font-weight: 500; font-size: 14.5px; fill: var(--ink); letter-spacing: .3px; }
  .step-letter { font-weight: 800; fill: var(--red-label); }
  .rule { stroke: var(--rule); stroke-width: 1; }
  .connector { stroke: var(--red-deep); stroke-width: 7; }
</style>
</head>
<body>
<svg class="flyer" viewBox="0 0 734 1036" xmlns="http://www.w3.org/2000/svg">
  <defs>
    <linearGradient id="hexFill" x1="0" y1="0" x2="1" y2="1">
      <stop offset="0" stop-color="#f0453a"/>
      <stop offset="1" stop-color="#b11c27"/>
    </linearGradient>
    <linearGradient id="valleyTone" x1="0" y1="0" x2="0.6" y2="1">
      <stop offset="0" stop-color="#f2b25a"/>
      <stop offset="0.35" stop-color="#b69a45"/>
      <stop offset="1" stop-color="#3f4a22"/>
    </linearGradient>
    <linearGradient id="towerTone" x1="0" y1="0" x2="1" y2="1">
      <stop offset="0" stop-color="#e8e9ea"/>
      <stop offset="0.55" stop-color="#8c8f93"/>
      <stop offset="0.85" stop-color="#d9875a"/>
      <stop offset="1" stop-color="#5f5650"/>
    </linearGradient>
    <g id="hex"><polygon points="0,-84 74,-42 74,42 0,84 -74,42 -74,-42" fill="url(#hexFill)"/></g>
    <g id="badge"><polygon points="0,-19 17,-9.5 17,9.5 0,19 -17,9.5 -17,-9.5" fill="#c9222b"/></g>
  </defs>

  <rect class="sheet" width="734" height="1036" fill="var(--paper)"/>

  <!-- header band -->
  <rect x="238" y="0" width="496" height="54" fill="var(--red-bright)"/>
  <rect x="238" y="54" width="496" height="80" fill="var(--red-deep)"/>
  <text class="title-small" x="462" y="48" font-size="39" text-anchor="middle">Client Journey</text>
  <text class="title-large" x="246" y="122" font-size="76">4 Summits</text>

  <!-- brand block -->
  <polyline points="0,140 120,205 238,134" fill="none" stroke="#e4e4e4" stroke-width="4"/>
  <rect x="112" y="46" width="24" height="24" fill="var(--red-bright)"/>
  <text class="brand-name" x="124" y="100" font-size="13" text-anchor="middle">BRAMWICK</text>
  <text class="brand-name" x="124" y="126" font-size="8.5" text-anchor="middle">BRAMWICK DEVELOPMENT</text>

  <!-- imagery panels -->
  <polygon role="img" aria-label="Photo of a winding road through green hills at sunset" points="0,308 224,328 224,560 0,700" fill="url(#valleyTone)"/>
  <polygon points="144,535 198,566 198,625 144,655 92,625 92,566" fill="#c2202a" opacity=".8"/>
  <polygon role="img" aria-label="Photo of a glass office tower seen from below" points="533,735 734,645 734,1036 533,978" fill="url(#towerTone)"/>
  <polygon points="547,985 580,1000 640,1036 610,1036 547,1000" fill="var(--red-bright)"/>
  <polygon points="570,1030 600,1036 570,1036" fill="var(--red-deep)"/>

  <!-- connectors -->
  <line class="connector" x1="319" y1="310" x2="319" y2="360"/>
  <line class="connector" x1="319" y1="500" x2="319" y2="560"/>
  <line class="connector" x1="250" y1="663" x2="180" y2="716"/>
  <line class="connector" x1="110" y1="830" x2="110" y2="875"/>

  <!-- stages -->
  <g transform="translate(319,236)"><use href="#hex"/><use href="#badge" y="-62"/>
    <text class="stage-num" y="-54" font-size="21">1.</text>
    <text class="stage-name" y="7" font-size="17">Basecamp</text></g>
  <g transform="translate(319,430)"><use href="#hex"/><use href="#badge" y="-62"/>
    <text class="stage-num" y="-54" font-size="21">2.</text>
    <text class="stage-name" y="-3" font-size="15">Summit 1 -</text>
    <text class="stage-name" y="16" font-size="13.5">PreConstruction</text></g>
  <g transform="translate(319,621)"><use href="#hex"/><use href="#badge" y="-62"/>
    <text class="stage-num" y="-54" font-size="21">3.</text>
    <text class="stage-name" y="-3" font-size="15">Summit 2 -</text>
    <text class="stage-name" y="16" font-size="14">Execution</text></g>
  <g transform="translate(110,757)"><use href="#hex"/><use href="#badge" y="-62"/>
    <text class="stage-num" y="-54" font-size="21">4.</text>
    <text class="stage-name" y="-10" font-size="15">Summit 3 -</text>
    <text class="stage-name" y="8" font-size="14">Project</text>
    <text class="stage-name" y="26" font-size="14">Management</text></g>
  <g transform="translate(110,945)"><use href="#hex"/><use href="#badge" y="-62"/>
    <text class="stage-num" y="-54" font-size="21">5.</text>
    <text class="stage-name" y="-6" font-size="15">Summit 4 -</text>
    <text class="stage-name" y="13" font-size="14">Completion</text></g>

  <!-- step lists -->
  <g class="steps-basecamp">
    <text class="step" x="412" y="209"><tspan class="step-letter">a.</tspan> Client Assessment</text>
    <line class="rule" x1="409" y1="216" x2="698" y2="216"/>
    <text class="step" x="412" y="238"><tspan class="step-letter">b.</tspan> Determine Project Goals</text>
    <text class="step" x="412" y="267"><tspan class="step-letter">c.</tspan> Proposal &amp; Fees</text>
  </g>
  <g class="steps-preconstruction">
    <text class="step" x="412" y="361"><tspan class="step-letter">a.</tspan> Develop Project Plan</text>
    <line class="rule" x1="409" y1="368" x2="698" y2="368"/>
    <text class="step" x="412" y="390"><tspan class="step-letter">b.</tspan> Develop Risk Assessment &amp; Plan</text>
    <text class="step" x="412" y="419"><tspan class="step-letter">c.</tspan> Devlelop Schedule</text>
    <line class="rule" x1="409" y1="427" x2="698" y2="427"/>
    <text class="step" x="412" y="448"><tspan class="step-letter">d.</tspan> Develop Budget</text>
    <text class="step" x="412" y="477"><tspan class="step-letter">e.</tspan> Develop Team</text>
    <line class="rule" x1="409" y1="487" x2="698" y2="487"/>
    <text class="step" x="412" y="506"><tspan class="step-letter">f.</tspan> GC, Sub, Consultants Contracts</text>
  </g>
  <g class="steps-execution">
    <text class="step" x="412" y="591"><tspan class="step-letter">a.</tspan> Acquire Permits</text>
    <line class="rule" x1="409" y1="598" x2="698" y2="598"/>
    <text class="step" x="412" y="620"><tspan class="step-letter">b.</tspan> PreConstruction Meeting</text>
    <line class="rule" x1="409" y1="629" x2="698" y2="629"/>
    <text class="step" x="412" y="649"><tspan class="step-letter">c.</tspan> Project Start</text>
  </g>
  <g class="steps-management">
    <text class="step" x="203" y="725"><tspan class="step-letter">a.</tspan> Shared Consciousness Meetings</text>
    <line class="rule" x1="200" y1="733" x2="488" y2="733"/>
    <text class="step" x="203" y="754"><tspan class="step-letter">b.</tspan> Pressurized Collaboration</text>
    <line class="rule" x1="200" y1="763" x2="488" y2="763"/>
    <text class="step" x="203" y="783"><tspan class="step-letter">c.</tspan> Schedule Management</text>
    <line class="rule" x1="200" y1="792" x2="488" y2="792"/>
    <text class="step" x="203" y="812"><tspan class="step-letter">d.</tspan> Run O.O.D.A. Loop</text>
    <line class="rule" x1="200" y1="823" x2="488" y2="823"/>
  </g>
  <g class="steps-completion">
    <line class="rule" x1="200" y1="929" x2="488" y2="929"/>
    <text class="step" x="203" y="947"><tspan class="step-letter">a.</tspan> Closeout</text>
    <line class="rule" x1="200" y1="954" x2="488" y2="954"/>
  </g>
</svg>
</body>
</html>
```